Postcard Design

We provide humorous speechwriting and presentation coaching services, primarily for the wedding market (best man, father of the bride, maid of honor). We'd like a design that incoporates the blue and white logo colors into a nice overall design, with the pitch:
"Use the power of humor to deliver the BEST speech of your life!"
Target Market(s)
Wedding market (best man, bride/groom)
Industry/Entity Type
Wedding
Requirements
Must have
- Bulletpoints for services provided:
- Speechwriting
- Presentation Coaching
- Emcee & Officiant Services
Listing of benefits provided:
- Conquer stage fright
- Deliver your speech like a pro
- Be funny AND tactful
- Leave them wanting more
Contact info -
Derek Hanslow
Derek@JollyQuill.com
www.JollyQuill.com
Testimonial quotes:
"People are STILL raving about that speech at our wedding. Thanks Jolly Quill!"
- Karen & Paul Dessaro, Baltimore, MD
"With the help of Jolly Quill, my best man speech brought down the house!"
- Trent Galloway, Melville, NY

```html
<!DOCTYPE html>
<html lang="en">
<head>
<meta charset="utf-8">
<title>Jolly Quill Postcard</title>
<link rel="stylesheet" href="https://fonts.googleapis.com/css2?family=Bebas+Neue&family=Raleway:wght@500&family=Source+Sans+3:ital,wght@0,600;0,700;1,600&family=Open+Sans:wght@600&display=swap">
<style>
  :root {
    --page-bg: #e6e6e6;
    --card-bg: #ffffff;
    --navy: #1f2a63;
    --navy-deep: #141b45;
    --navy-light: #2e3f86;
    --ink-white: #ffffff;
    --ink-soft: #d9def0;
    --photo-light: #f4f4f4;
    --photo-mid: #cfcfcf;
    --photo-dark: #1b1b1b;
  }
  * { margin: 0; padding: 0; box-sizing: border-box; }
  html, body {
    width: 1200px; height: 900px; overflow: hidden;
    background: var(--page-bg);
  }
  .postcard {
    position: absolute; left: 200px; top: 115px;
    width: 830px; height: 640px;
    background: var(--card-bg);
    box-shadow: 3px 4px 6px rgba(0,0,0,0.35);
    overflow: hidden;
  }
  .postcard-shapes { position: absolute; inset: 0; }

  .brand {
    position: absolute; left: 30px; top: 13px;
    width: 130px; height: 130px;
    display: flex; align-items: center; justify-content: center;
  }
  .brand-name {
    font-family: "Source Sans 3", sans-serif; font-weight: 700;
    font-size: 18px; line-height: 20px; text-align: center;
    color: var(--ink-white); letter-spacing: 0.5px;
  }

  .pitch, .benefits, .web {
    position: absolute; color: var(--ink-white); white-space: nowrap;
  }
  .pitch-small { font-family: "Raleway", sans-serif; font-weight: 500; }
  .pitch-big { font-family: "Bebas Neue", sans-serif; line-height: 1; }
  .p1 { left: 500px; top: 34px; font-size: 29px; }
  .p2 { left: 500px; top: 72px; font-size: 104px; letter-spacing: 1px; }
  .p3 { left: 555px; top: 165px; font-size: 29px; }
  .p4 { left: 551px; top: 210px; font-size: 52px; }
  .p5 { left: 549px; top: 255px; font-size: 102px; }
  .p6 { left: 559px; top: 348px; font-size: 36px; }

  .benefits {
    left: 560px; top: 418px; width: 270px; text-align: center;
    font-family: "Source Sans 3", sans-serif; font-weight: 700;
  }
  .benefit-lead { font-size: 23px; line-height: 26px; display: block; }
  .benefit-sub { font-size: 17px; line-height: 22px; display: block; }

  .web {
    left: 640px; top: 583px;
    font-family: "Open Sans", sans-serif; font-weight: 600; font-size: 15px;
    transform: rotate(12deg); transform-origin: left center;
    letter-spacing: 0.3px;
  }

  .photo-notes {
    position: absolute; left: 32px; top: 418px; width: 470px;
    font-family: "Source Sans 3", sans-serif; color: var(--ink-white);
  }
  .services {
    list-style: none; display: flex; flex-wrap: wrap; gap: 4px 10px;
    font-size: 13px; font-weight: 700; line-height: 18px;
    text-transform: uppercase; letter-spacing: 0.3px;
    margin-bottom: 12px;
  }
  .services li { display: flex; align-items: center; gap: 5px; }
  .services svg { width: 12px; height: 12px; flex: none; }
  .testimonial { margin-bottom: 9px; }
  .testimonial-quote {
    font-size: 15px; font-weight: 600; font-style: italic; line-height: 18px;
  }
  .testimonial-author {
    display: block; font-size: 12px; font-weight: 600; font-style: normal;
    line-height: 16px; color: var(--ink-soft); margin-top: 2px;
  }
  .contact {
    font-size: 14px; font-weight: 700; line-height: 18px; margin-top: 4px;
  }
  .contact-sep { margin: 0 6px; color: var(--ink-soft); }
</style>
</head>
<body>
  <div class="postcard">
    <svg class="postcard-shapes" width="830" height="640" viewBox="0 0 830 640">
      <defs>
        <linearGradient id="photoTone" x1="0" y1="0" x2="0" y2="1">
          <stop offset="0" stop-color="var(--photo-light)"/>
          <stop offset="0.3" stop-color="var(--photo-mid)"/>
          <stop offset="0.58" stop-color="#3a3a3a"/>
          <stop offset="1" stop-color="var(--photo-dark)"/>
        </linearGradient>
        <linearGradient id="panelTone" x1="0" y1="0" x2="0.3" y2="1">
          <stop offset="0" stop-color="var(--navy-deep)"/>
          <stop offset="0.5" stop-color="var(--navy)"/>
          <stop offset="1" stop-color="var(--navy-light)"/>
        </linearGradient>
      </defs>
      <rect x="15" y="55" width="495" height="585" fill="url(#photoTone)" role="img" aria-label="Photo: smiling groomsman in a tuxedo raising a glass of champagne while reading toast notes"/>
      <polygon points="295,0 380,0 372,14" fill="var(--navy-deep)"/>
      <polygon points="365,0 830,0 830,604 595,550" fill="url(#panelTone)"/>
      <polygon points="620,560 830,605 830,640 645,640" fill="var(--navy-deep)"/>
      <circle cx="95" cy="78" r="64" fill="var(--navy)"/>
    </svg>

    <div class="brand"><span class="brand-name">JOLLY<br>QUILL</span></div>

    <div class="pitch pitch-small p1">Use the power of</div>
    <div class="pitch pitch-big p2">HUMOR</div>
    <div class="pitch pitch-small p3">to deliver the</div>
    <div class="pitch pitch-big p4">BEST</div>
    <div class="pitch pitch-big p5">SPEECH</div>
    <div class="pitch pitch-small p6">of your life</div>

    <div class="benefits">
      <span class="benefit-lead">Conquer stage fright</span>
      <span class="benefit-sub">Deliver your speech like a pro</span>
      <span class="benefit-lead">Be funny &amp; tactful</span>
      <span class="benefit-sub">Leave them wanting more</span>
    </div>

    <div class="photo-notes">
      <ul class="services">
        <li><svg viewBox="0 0 12 12"><path d="M1.5 6.5 L4.5 9.5 L10.5 2.5" fill="none" stroke="#fff" stroke-width="2"/></svg>Speechwriting</li>
        <li><svg viewBox="0 0 12 12"><path d="M1.5 6.5 L4.5 9.5 L10.5 2.5" fill="none" stroke="#fff" stroke-width="2"/></svg>Presentation Coaching</li>
        <li><svg viewBox="0 0 12 12"><path d="M1.5 6.5 L4.5 9.5 L10.5 2.5" fill="none" stroke="#fff" stroke-width="2"/></svg>Emcee &amp; Officiant Services</li>
      </ul>
      <blockquote class="testimonial">
        <p class="testimonial-quote">“People are STILL raving about that speech at our wedding. Thanks Jolly Quill!”</p>
        <cite class="testimonial-author">— Karen &amp; Paul Dessaro, Baltimore, MD</cite>
      </blockquote>
      <blockquote class="testimonial">
        <p class="testimonial-quote">“With the help of Jolly Quill, my best man speech brought down the house!”</p>
        <cite class="testimonial-author">— Trent Galloway, Melville, NY</cite>
      </blockquote>
      <p class="contact">Derek Hanslow<span class="contact-sep">|</span>Derek@JollyQuill.com</p>
    </div>

    <div class="web">www.JollyQuill.com</div>
  </div>
</body>
</html>
```